Machine Sign

This is for a laundromat. I would like signs to hang above the machines from the ceiling indicating machine size. For example we have 6 loaders, 4 loaders, 2 loaders.

```html
<!DOCTYPE html>
<html lang="en">
<head>
<meta charset="UTF-8">
<title>Machine Size Sign – 4 Loaders</title>
<link rel="stylesheet" href="https://fonts.googleapis.com/css2?family=Arimo:wght@700&display=swap">
<style>
  :root {
    --page-bg: #e9ecf1;
    --sign-white: #ffffff;
    --sign-edge: #d3d7de;
    --sign-purple: #3b2f8c;
    --sign-blue: #0a8fd6;
    --sign-text: #ffffff;
  }
  html, body {
    margin: 0;
    padding: 0;
    width: 1200px;
    height: 900px;
    overflow: hidden;
    background: var(--page-bg);
  }
  .canvas {
    width: 1200px;
    height: 900px;
    display: flex;
    align-items: center;
    justify-content: center;
  }
  .machine-sign {
    width: 836px;
    height: 813px;
    display: block;
  }
  .sign-frame { fill: var(--sign-white); stroke: var(--sign-edge); stroke-width: 1; }
  .sign-field { fill: var(--sign-purple); }
  .sign-chevron { fill: var(--sign-blue); }
  .sign-number,
  .sign-label {
    font-family: "Arimo", Arial, Helvetica, sans-serif;
    font-weight: 700;
    fill: var(--sign-text);
    text-anchor: middle;
  }
  .sign-number { font-size: 168px; }
  .sign-label { font-size: 86px; }
</style>
</head>
<body>
  <main class="canvas">
    <svg class="machine-sign" viewBox="0 0 576 560" role="img" aria-label="Hanging sign: 4 Loaders">
      <polygon class="sign-frame" points="0.5,0.5 575.5,0.5 575.5,398 288,559.5 0.5,398"/>
      <polygon class="sign-field" points="15,15 561,15 561,295 288,442 15,295"/>
      <polygon class="sign-chevron" points="15,295 288,442 561,295 561,390 288,540 15,390"/>
      <text class="sign-number" x="288" y="170">4</text>
      <text class="sign-label" x="288" y="262">LOADERS</text>
    </svg>
  </main>
</body>
</html>
```